Harlan Whitcombe Accounting Flyer

A one page flyer to promote our 2009 season taxation return price of $95.00 GST Inclusive. Some text items we do require on the flyer are as follows:

- Two office addresses & phone numbers - 21 King Street Scottsdale - 03 61847203 & 5/62 Tindall Road George Town - 03 61590836

  - Basic Individual taxation returns completed for just $95* - just mention this offer when booking an appointment or dropping off your information. We will lodge your return electronically for you as well - no extra charge!

Does not include supplemental work such as taxpayers with rental properties or supplementary schedule requirements which will incur extra fees.
Updates

Please make sure the firm''s name is included in the flyer and the words - taxation return - only is required not the year it is for ie: 2009.

The firm name and contacts need to be prominately displayed to ensure clients are drawn to the firm and can contact us easily.
The price is also an important feature as this is the main thing clients are interested in for this type of work.

Target Market(s)

General public who require Individual taxation returns.  

Industry/Entity Type

Accounting

Requirements
Must have
• Disclaimers as listed in the ''''describe what you want'''' box.
Nice to have
• Brightly coloured, professional modern feel about the graphics, surprise us!
Should not have
• Any animated characters.

```html
<!DOCTYPE html>
<html lang="en">
<head>
<meta charset="utf-8">
<title>Harlan Whitcombe Accounting – Taxation Return Flyer</title>
<link rel="stylesheet" href="https://fonts.googleapis.com/css2?family=Montserrat:ital,wght@0,500;0,600;0,700;1,500&display=swap">
<style>
  :root {
    --blue-deep: #1d3f9a;
    --blue-mid: #1f5bb8;
    --blue-glow: #2a72c8;
    --silver-light: #f2f3f5;
    --silver-mid: #c9ccd1;
    --silver-dark: #9ea3aa;
    --white: #ffffff;
    --red: #be1e2d;
    --red-light: #d4503a;
    --yellow: #ffe600;
    --navy-text: #1c4a9c;
  }
  * { margin: 0; padding: 0; box-sizing: border-box; }
  html, body { width: 846px; height: 1200px; overflow: hidden; background: var(--silver-mid); }
  .flyer {
    position: relative;
    width: 846px;
    height: 1200px;
    overflow: hidden;
    font-family: "Montserrat", Arial, sans-serif;
    background: linear-gradient(180deg, #b9bdc3 0%, #e6e7ea 40%, #c4c7cc 100%);
  }
  .band-top, .band-bottom { position: absolute; left: 0; width: 846px; }
  .band-top { top: 0; height: 74px; }
  .band-bottom { bottom: 0; height: 78px; }
  .panel {
    position: absolute;
    top: 74px; left: 0;
    width: 846px; height: 1048px;
    background: radial-gradient(ellipse 60% 45% at 50% 42%, var(--blue-glow) 0%, var(--blue-mid) 45%, var(--blue-deep) 100%);
    text-align: center;
    color: var(--white);
  }
  .firm-name {
    position: absolute; top: 46px; left: 0; width: 100%;
    font-size: 34px; font-weight: 600; letter-spacing: 0.3px;
  }
  .headline { position: absolute; left: 0; width: 100%; font-weight: 700; line-height: 1;
    background: linear-gradient(180deg, var(--white) 0%, var(--silver-light) 45%, var(--silver-dark) 100%);
    -webkit-background-clip: text; background-clip: text; color: transparent;
    filter: drop-shadow(0 3px 4px rgba(0,0,0,0.35));
  }
  .headline-taxation { top: 140px; font-size: 77px; letter-spacing: 1px; }
  .headline-return { top: 216px; font-size: 132px; letter-spacing: 2px; }
  .price-badge { position: absolute; left: 279px; top: 382px; width: 288px; height: 288px; }
  .offer-copy {
    position: absolute; left: 133px; top: 702px; width: 590px;
    text-align: left; font-size: 17.5px; font-weight: 500; line-height: 23.5px;
  }
  .disclaimer {
    position: absolute; left: 133px; top: 814px; width: 560px;
    text-align: left; font-size: 15.5px; font-style: italic; font-weight: 500; line-height: 22px;
  }
  .contact-card {
    position: absolute; left: 150px; top: 923px; width: 547px; height: 83px;
    border-radius: 10px;
    background: linear-gradient(180deg, #ffffff 0%, #eef0f3 55%, #cfd2d7 100%);
    box-shadow: 0 4px 10px rgba(0,0,0,0.35);
    color: var(--navy-text);
    font-size: 17.5px; font-weight: 500; line-height: 25px;
    font-style: normal;
    padding-top: 16px;
  }
  .phone-icon { font-size: 15px; margin: 0 2px 0 4px; }
</style>
</head>
<body>
<div class="flyer">
  <svg class="band-top" viewBox="0 0 846 74" aria-hidden="true">
    <path d="M0 34 C260 6 560 8 846 40 L846 0 L0 0 Z" fill="#f3f4f6" opacity="0.7"/>
  </svg>

  <main class="panel">
    <p class="firm-name">Harlan Whitcombe Accounting</p>
    <h1>
      <span class="headline headline-taxation">TAXATION</span>
      <span class="headline headline-return">RETURN!</span>
    </h1>

    <svg class="price-badge" viewBox="-144 -144 288 288" role="img" aria-label="Just $95 GST Inclusive">
      <defs>
        <linearGradient id="badgeRed" x1="0" y1="0" x2="1" y2="1">
          <stop offset="0.5" stop-color="#d4503a"/>
          <stop offset="0.5" stop-color="#be1e2d"/>
        </linearGradient>
      </defs>
      <g fill="#ffe600">
        <rect x="-99" y="-99" width="198" height="198"/>
        <rect x="-99" y="-99" width="198" height="198" transform="rotate(11.25)"/>
        <rect x="-99" y="-99" width="198" height="198" transform="rotate(22.5)"/>
        <rect x="-99" y="-99" width="198" height="198" transform="rotate(33.75)"/>
        <rect x="-99" y="-99" width="198" height="198" transform="rotate(45)"/>
        <rect x="-99" y="-99" width="198" height="198" transform="rotate(56.25)"/>
        <rect x="-99" y="-99" width="198" height="198" transform="rotate(67.5)"/>
        <rect x="-99" y="-99" width="198" height="198" transform="rotate(78.75)"/>
      </g>
      <g fill="url(#badgeRed)">
        <rect x="-89" y="-89" width="178" height="178"/>
        <rect x="-89" y="-89" width="178" height="178" transform="rotate(11.25)"/>
        <rect x="-89" y="-89" width="178" height="178" transform="rotate(22.5)"/>
        <rect x="-89" y="-89" width="178" height="178" transform="rotate(33.75)"/>
        <rect x="-89" y="-89" width="178" height="178" transform="rotate(45)"/>
        <rect x="-89" y="-89" width="178" height="178" transform="rotate(56.25)"/>
        <rect x="-89" y="-89" width="178" height="178" transform="rotate(67.5)"/>
        <rect x="-89" y="-89" width="178" height="178" transform="rotate(78.75)"/>
      </g>
      <g font-family="Montserrat, Arial, sans-serif" font-weight="700" text-anchor="middle">
        <text x="0" y="-44" font-size="30" fill="#ffe600">JUST</text>
        <text x="0" y="36" font-size="76" fill="#ffe600">$95</text>
        <text x="0" y="66" font-size="16" font-weight="600" fill="#ffffff">GST Inclusive</text>
      </g>
    </svg>

    <p class="offer-copy">Basic Individual taxation returns completed for just $95*- just mention this offer when booking an appointment or dropping off your information. We will lodge your return electronically for you as well - no extra charge!</p>
    <p class="disclaimer">Does not include supplemental work such as taxpayers with rental properties or supplementary schedule requirements which will incur extra fees.</p>

    <address class="contact-card">
      <div class="office">47 Penrose Lane Scottsdale <span class="phone-icon">✆</span>03 61847203</div>
      <div class="office">5/62 Tindall Road George Town <span class="phone-icon">✆</span>03 61590836</div>
    </address>
  </main>

  <svg class="band-bottom" viewBox="0 0 846 78" aria-hidden="true">
    <path d="M0 30 C280 60 560 54 846 20 L846 78 L0 78 Z" fill="#e9eaed" opacity="0.6"/>
  </svg>
</div>
</body>
</html>
```